Halvering Family Dentistry
Peter K. Wadlow, DDS
Project: Halvering Family Dentistry
Halvering Family Dentistry -
Creative Brief
Professional
7182 Quillan Road, Unit C Brenford, KY 40317
smyle7q@postvale.net

```html
<!DOCTYPE html>
<html lang="en">
<head>
<meta charset="utf-8">
<title>Halvering Family Dentistry – Business Cards</title>
<link rel="stylesheet" href="https://fonts.googleapis.com/css2?family=Marcellus&family=Open+Sans:wght@400;600;700&display=swap">
<style>
  :root {
    --bg: #ecebe8;
    --card: #ffffff;
    --ink: #2b2b2b;
    --muted: #4a4a4a;
    --green: #1f8a3a;
    --rule: #c9c9c9;
    --shadow: rgba(0,0,0,0.14);
  }
  * { box-sizing: border-box; margin: 0; padding: 0; }
  html, body { width: 1200px; height: 852px; overflow: hidden; }
  body {
    background: var(--bg);
    font-family: "Open Sans", Arial, sans-serif;
    color: var(--ink);
    display: flex;
    flex-direction: column;
    align-items: center;
    justify-content: center;
    gap: 44px;
  }
  .card {
    width: 600px;
    height: 343px;
    background: var(--card);
    border-radius: 22px;
    box-shadow: 0 6px 18px var(--shadow);
    position: relative;
  }

  /* shared brand block */
  .brand { display: flex; align-items: center; gap: 12px; }
  .brand-dot {
    width: 34px; height: 34px; border-radius: 50%;
    background: var(--green); flex: none;
  }
  .brand-name {
    font-family: "Marcellus", Georgia, serif;
    color: var(--ink);
    line-height: 1.02;
    text-transform: uppercase;
  }
  .tagline {
    font-family: "Marcellus", Georgia, serif;
    text-transform: uppercase;
    color: var(--ink);
    letter-spacing: 0.02em;
    white-space: nowrap;
  }
  .doctor { color: var(--green); font-weight: 700; }
  .address { color: var(--muted); line-height: 1.45; }
  .contact { list-style: none; color: var(--muted); }
  .contact li { display: flex; align-items: center; gap: 8px; }
  .contact svg { flex: none; fill: var(--green); }

  /* card one: split layout */
  .card--split { display: flex; align-items: center; }
  .card--split .identity { width: 300px; padding-left: 48px; }
  .card--split .brand-name { font-size: 22px; }
  .card--split .tagline { font-size: 9.5px; margin-top: 8px; }
  .card--split .divider {
    width: 1px; height: 150px; background: var(--rule);
  }
  .card--split .details { padding-left: 28px; }
  .card--split .doctor { font-size: 17px; margin-bottom: 22px; }
  .card--split .address { font-size: 12.5px; margin-bottom: 16px; }
  .card--split .contact { font-size: 12.5px; }
  .card--split .contact li + li { margin-top: 5px; }

  /* card two: centred layout */
  .card--centred { display: flex; flex-direction: column; align-items: center; padding-top: 58px; }
  .card--centred .brand-name { font-size: 31px; }
  .card--centred .brand-dot { width: 46px; height: 46px; }
  .card--centred .tagline { font-size: 12px; margin-top: 10px; }
  .card--centred .doctor { font-size: 18px; margin-top: 26px; }
  .card--centred .footer { display: flex; align-items: center; margin-top: 16px; }
  .card--centred .address { font-size: 12.5px; text-align: left; padding-right: 20px; }
  .card--centred .divider { width: 1px; height: 48px; background: var(--rule); }
  .card--centred .contact { font-size: 12.5px; padding-left: 20px; }
  .card--centred .contact li + li { margin-top: 4px; }
</style>
</head>
<body>

  <article class="card card--split">
    <div class="identity">
      <div class="brand">
        <span class="brand-dot"></span>
        <p class="brand-name">Halvering<br>Family Dentistry</p>
      </div>
      <p class="tagline">Caring for gentle bright smiles since 1991</p>
    </div>
    <div class="divider"></div>
    <div class="details">
      <p class="doctor">Peter K. Wadlow, DDS</p>
      <p class="address">7182 Quillan Road, Unit C<br>Brenford, KY 40317</p>
      <ul class="contact">
        <li><svg width="12" height="12" viewBox="0 0 24 24" aria-hidden="true"><path d="M6.6 10.8a15 15 0 0 0 6.6 6.6l2.2-2.2a1 1 0 0 1 1-.25 11.4 11.4 0 0 0 3.6.57 1 1 0 0 1 1 1V20a1 1 0 0 1-1 1A17 17 0 0 1 3 4a1 1 0 0 1 1-1h3.5a1 1 0 0 1 1 1c0 1.25.2 2.45.57 3.6a1 1 0 0 1-.25 1z"/></svg>502-555-0148</li>
        <li><svg width="12" height="12" viewBox="0 0 24 24" aria-hidden="true"><path d="M2 5h20v14H2zm2 2v.5l8 5 8-5V7l-8 5z"/></svg>smyle7q@postvale.net</li>
      </ul>
    </div>
  </article>

  <article class="card card--centred">
    <div class="brand">
      <span class="brand-dot"></span>
      <p class="brand-name">Halvering<br>Family Dentistry</p>
    </div>
    <p class="tagline">Caring for gentle bright smiles since 1991</p>
    <p class="doctor">Peter K. Wadlow, DDS</p>
    <div class="footer">
      <p class="address">7182 Quillan Road, Unit C<br>Brenford, KY 40317</p>
      <div class="divider"></div>
      <ul class="contact">
        <li><svg width="12" height="12" viewBox="0 0 24 24" aria-hidden="true"><path d="M6.6 10.8a15 15 0 0 0 6.6 6.6l2.2-2.2a1 1 0 0 1 1-.25 11.4 11.4 0 0 0 3.6.57 1 1 0 0 1 1 1V20a1 1 0 0 1-1 1A17 17 0 0 1 3 4a1 1 0 0 1 1-1h3.5a1 1 0 0 1 1 1c0 1.25.2 2.45.57 3.6a1 1 0 0 1-.25 1z"/></svg>502-555-0148</li>
        <li><svg width="12" height="12" viewBox="0 0 24 24" aria-hidden="true"><path d="M2 5h20v14H2zm2 2v.5l8 5 8-5V7l-8 5z"/></svg>smyle7q@postvale.net</li>
      </ul>
    </div>
  </article>

</body>
</html>
```